Flyer for family counseling

For my family counseling I'm looking for a design for flyers. Important is not only the appearance of the flyer, but also the content design. All important contents can be found on my website: www.brigitte-volkanter.at The following items should NOT appear on the flyer: - constellation work - bereavement and palliative work My logo should definitely be on the flyer. Source files are available.

Target Market(s)

Families, individuals, children, couples in need of psychological support.

Colors

Designer to choose colors to be used in the design.

Requirements
Must have
• My logo - source files available Website and contact data Recognition value from website to flyer and vice versa
Should not have
• Mention of the constellation work and mourning and palliative work not desired.

```html
<!DOCTYPE html>
<html lang="de">
<head>
<meta charset="utf-8">
<title>Familienberatung Lindenau – Flyer</title>
<link rel="stylesheet" href="https://fonts.googleapis.com/css2?family=Oxygen:wght@400;700&family=Open+Sans:ital,wght@0,400;0,600;1,400&display=swap">
<style>
  :root {
    --teal: #2bb8aa;
    --teal-dark: #1a9d91;
    --teal-light: #3fd0c1;
    --ink: #2a2a2a;
    --paper: #fbfbfb;
    --stage: #e4e4e4;
    --photo-warm: #d8b48a;
    --photo-warm-2: #a87b52;
  }
  * { box-sizing: border-box; margin: 0; padding: 0; }
  html, body { width: 1200px; height: 1000px; overflow: hidden; }
  body {
    background: var(--stage);
    font-family: "Open Sans", sans-serif;
    color: var(--ink);
    position: relative;
  }
  .flyer {
    position: absolute;
    left: 250px; top: 20px;
    width: 700px; height: 960px;
    background: var(--paper);
    box-shadow: 0 6px 24px rgba(0,0,0,.18);
    overflow: hidden;
  }
  /* header */
  .header { position: absolute; left: 0; top: 0; width: 100%; height: 118px; }
  .brand {
    position: absolute; left: 30px; top: 34px;
    display: flex; align-items: center; gap: 12px;
  }
  .brand-dot { width: 34px; height: 34px; border-radius: 50%; background: var(--teal); }
  .brand-name {
    font-family: "Oxygen", sans-serif; font-size: 19px; font-weight: 400;
    color: var(--teal-dark); letter-spacing: 1px;
  }
  .url-bar {
    position: absolute; right: 0; top: 44px; height: 38px;
    display: flex; gap: 7px;
  }
  .url-bar .sq { width: 28px; height: 38px; background: var(--teal); }
  .url-bar .sq.light { background: var(--teal-light); }
  .url-bar .url {
    background: var(--teal); color: #fff; height: 38px;
    padding: 0 22px 0 18px; display: flex; align-items: center;
    font-family: "Oxygen", sans-serif; font-size: 21px; letter-spacing: .5px;
  }
  /* hero */
  .hero { position: absolute; left: 0; top: 118px; width: 100%; height: 318px; }
  .hero-photo {
    width: 100%; height: 100%;
    background: linear-gradient(100deg, #f1e2c9 0%, var(--photo-warm) 45%, #c7955f 70%, #e9d2b2 100%);
  }
  .hero-label {
    position: absolute; left: 0; bottom: 22px; height: 42px;
    display: flex; gap: 7px;
  }
  .hero-label .title {
    background: var(--teal-light); color: #fff; padding: 0 18px 0 12px;
    display: flex; align-items: center; white-space: nowrap;
    font-family: "Oxygen", sans-serif; font-size: 21px;
  }
  .hero-label .sq { width: 44px; background: var(--teal-light); }
  .hero-label .sq.dark { background: var(--teal); }
  /* services */
  .services {
    position: absolute; left: 22px; top: 458px; width: 656px;
    display: grid; grid-template-columns: 1fr 1fr; column-gap: 22px; row-gap: 22px;
  }
  .service { display: flex; gap: 10px; align-items: flex-start; }
  .service-photo {
    flex: 0 0 140px; height: 94px;
    border-radius: 0 0 18px 0;
    background: linear-gradient(135deg, #efe6d8, var(--photo-warm) 60%, var(--photo-warm-2));
  }
  .service h3 {
    font-family: "Oxygen", sans-serif; font-size: 14px; font-weight: 700;
    color: var(--teal-dark); margin-bottom: 3px;
  }
  .service p { font-size: 8.4px; line-height: 1.35; text-align: justify; }
  /* testimonials */
  .voices {
    position: absolute; left: 0; top: 720px; width: 100%; height: 196px;
    background: var(--teal);
  }
  .voices h2 {
    position: absolute; left: 32px; top: 14px;
    font-family: "Oxygen", sans-serif; font-weight: 400; font-size: 21px; color: #fff;
  }
  .quotes {
    position: absolute; left: 36px; top: 56px; width: 630px;
    display: grid; grid-template-columns: 1fr 1fr; gap: 36px;
  }
  .quote {
    position: relative; background: #fff; height: 90px; padding: 14px 14px 10px;
    font-size: 9.3px; font-style: italic; line-height: 1.35;
  }
  .quote cite {
    position: absolute; right: 18px; bottom: 8px;
    font-style: normal; font-size: 9.5px;
  }
  .quote .mark {
    position: absolute; font-family: "Oxygen", sans-serif; font-weight: 700; font-style: normal;
    font-size: 44px; color: var(--teal-light); line-height: 1;
  }
  .quote .mark.open { left: -18px; top: -12px; }
  .quote .mark.close { right: -18px; bottom: -30px; }
  .contact {
    position: absolute; left: 0; bottom: 0; width: 100%; height: 44px;
    background: var(--teal-light); color: #fff;
    display: flex; align-items: center; padding-left: 34px; white-space: nowrap;
    font-family: "Oxygen", sans-serif; font-size: 11.5px; font-weight: 700;
  }
</style>
</head>
<body>
<main class="flyer">
  <header class="header">
    <div class="brand">
      <span class="brand-dot"></span>
      <span class="brand-name">Brigitte Volkanter</span>
    </div>
    <div class="url-bar">
      <span class="sq"></span>
      <span class="sq light"></span>
      <span class="url">www.brigitte-volkanter.at</span>
    </div>
  </header>

  <section class="hero">
    <div class="hero-photo" role="img" aria-label="Foto: Beratungsgespräch mit einer Familie in einem hellen Raum"></div>
    <div class="hero-label">
      <span class="title">Familienberatung Lindenau</span>
      <span class="sq"></span>
      <span class="sq dark"></span>
    </div>
  </section>

  <section class="services">
    <article class="service">
      <div class="service-photo" role="img" aria-label="Foto: Einzelgespräch im Beratungsraum"></div>
      <div>
        <h3>Einzelberatung</h3>
        <p>Für den ganz persönlichen Weg zur Selbstbestimmung. Ist er einmal betreten, wird die persönliche Entwicklung ein wundervolles Abenteuer.</p>
      </div>
    </article>
    <article class="service">
      <div class="service-photo" role="img" aria-label="Foto: Paar im Gespräch mit der Beraterin"></div>
      <div>
        <h3>Paarberatung</h3>
        <p>Muster können aufgelöst werden! Gerne unterstütze ich Sie auf Ihrem Weg, sich in Ihrer Partnerschaft wieder auf deren Grundlage zu besinnen. Darauf aufzubauen, einen viel versprechenden Neubeginn zu wagen.</p>
      </div>
    </article>
    <article class="service">
      <div class="service-photo" role="img" aria-label="Foto: Eltern und Kinder beim gemeinsamen Spielen"></div>
      <div>
        <h3>Erziehungsberatung</h3>
        <p>Meine Aufgabe besteht darin, Sie in einem vertrauensvollen Rahmen zu unterstützen, eine neue Form der elterlichen Kooperation zu finden und Ihren Blick und Ihre Aufmerksamkeit auf die Bedürfnisse und Nöte der Kinder/des Kindes zu richten.</p>
      </div>
    </article>
    <article class="service">
      <div class="service-photo" role="img" aria-label="Foto: Mutter und Töchter lesen gemeinsam ein Buch"></div>
      <div>
        <h3>Familie &amp; Kinder</h3>
        <p>Das Ziel einer Familientherapie ist, eine positive Beziehungsveränderung zwischen den einzelnen Familienmitgliedern zu erreichen. Respekt, gegenseitiges Verständnis und Einfühlungsvermögen füreinander sind wesentlich für ein funktionierendes Zusammenleben in einer Familie.</p>
      </div>
    </article>
  </section>

  <section class="voices">
    <h2>Stimmen von Klienten</h2>
    <div class="quotes">
      <blockquote class="quote">
        <span class="mark open">“</span>
        Brigitte Volkanter zeichnet sich durch Wärme, Souveränität, Ruhe und Sorgfältigkeit aus. Sicher und liebevoll begleitet sie durch den Prozess. Sie ist neutral, aber interessiert. Man fühlt sich gut aufgehoben, auch wenn es "ans Eingemachte" geht.
        <cite>Frau R. Klientin</cite>
        <span class="mark close">”</span>
      </blockquote>
      <blockquote class="quote">
        <span class="mark open">“</span>
        Mein Weg war voller Steine und Holz. Ich nahm den Besen in die Hand und kehrte. Frau Volkanter begleitete mich dabei.
        <cite>Frau H. Klientin</cite>
        <span class="mark close">”</span>
      </blockquote>
    </div>
  </section>

  <footer class="contact">
    Lindenweg 12/3, 1160 Vienna | familienberatung@brigitte-volkanter.at | Telephone: +43 676 418 27 90
  </footer>
</main>
</body>
</html>
```